Business card and stationary for a natural medicine company
Herbal drug by plant biotechnology company
Business card and stationary for a natural medicine company - Pharmacy/Pharmaceuticals
Creative Brief
Professional
Soojin Park
President
5817 Briarwood DR Fort Wayne, IN 46825 USA
president@verdolith.com
www.verdolith.com
Please use the catch phrase "New Drugs from Herbal Medicines"
Please print following verse. And by the river upon the bank thereof, on this side and on that side, shall grow all trees for meat, whose leaf shall not fade, neither shall the fruit thereof be consumed: it shall bring forth new fruit according to his months, because their waters they issued out of the sanctuary: and the fruit thereof shall be for meat, and the leaf thereof for medicine. Ezekiel 47:12

```html
<!DOCTYPE html>
<html lang="en">
<head>
<meta charset="utf-8">
<title>Verdolith Business Card</title>
<link href="https://fonts.googleapis.com/css2?family=Marcellus+SC&display=swap" rel="stylesheet">
<style>
  :root {
    --page-bg: #e9ecef;
    --card-bg: #ffffff;
    --brand-blue: #1f6fb8;
    --deep-blue: #1a3f8f;
    --sky-blue: #3fa8e6;
    --leaf-green: #5cae2e;
    --text-dark: #2b3f6e;
    --text-muted: #4a5568;
    --divider: #b9c2cf;
    --on-blue: #ffffff;
  }
  * { box-sizing: border-box; margin: 0; padding: 0; }
  html, body {
    width: 1200px; height: 901px; overflow: hidden;
    background: var(--page-bg);
    font-family: "Marcellus SC", serif;
  }
  .business-card {
    position: absolute; left: 100px; top: 160px;
    width: 1000px; height: 580px;
    background: var(--card-bg);
    border-radius: 44px;
    overflow: hidden;
    box-shadow: 0 12px 30px rgba(0,0,0,0.15);
  }
  .card-wave { position: absolute; left: 0; top: 280px; width: 1000px; height: 300px; }
  .brand {
    position: absolute; left: 0; right: 0; top: 40px;
    display: flex; justify-content: center; align-items: center; gap: 18px;
  }
  .brand-square {
    width: 78px; height: 78px; border-radius: 14px;
    background: var(--sky-blue);
  }
  .brand-name { font-size: 52px; color: var(--brand-blue); letter-spacing: 1px; }
  .tagline {
    position: absolute; left: 0; right: 0; top: 136px;
    text-align: center; font-size: 20px; color: var(--leaf-green); letter-spacing: 1px;
  }
  .identity {
    position: absolute; right: 520px; top: 190px;
    text-align: right; color: var(--text-dark);
  }
  .person-name { font-size: 28px; color: var(--brand-blue); letter-spacing: 2px; }
  .person-title { font-size: 20px; margin-top: 4px; color: var(--text-muted); }
  .address { font-size: 21px; margin-top: 20px; line-height: 1.4; color: var(--text-dark); }
  .divider {
    position: absolute; left: 500px; top: 190px;
    width: 1px; height: 150px; background: var(--divider);
  }
  .contacts {
    position: absolute; left: 522px; top: 190px;
    list-style: none; color: var(--text-dark); font-size: 21px;
  }
  .contacts li { display: flex; align-items: center; gap: 10px; height: 28px; }
  .contacts li.gap-before { margin-top: 10px; }
  .contact-icon { width: 18px; height: 18px; flex: none; }
  .verse {
    position: absolute; left: 60px; right: 60px; bottom: 16px;
    text-align: center; color: var(--on-blue);
    font-size: 11px; line-height: 15px; letter-spacing: 0.2px;
  }
</style>
</head>
<body>
  <div class="business-card">
    <svg class="card-wave" viewBox="0 0 1000 300" preserveAspectRatio="none" aria-hidden="true">
      <defs>
        <linearGradient id="waveBlue" x1="0" y1="0" x2="1" y2="0">
          <stop offset="0" stop-color="#1a3f8f"/>
          <stop offset="0.5" stop-color="#2d7fd0"/>
          <stop offset="1" stop-color="#3fa8e6"/>
        </linearGradient>
      </defs>
      <path d="M0 40 C 250 130, 550 200, 1000 150 L1000 300 L0 300 Z" fill="#5cae2e"/>
      <path d="M0 58 C 250 148, 550 218, 1000 168 L1000 300 L0 300 Z" fill="#ffffff"/>
      <path d="M0 74 C 250 164, 550 234, 1000 184 L1000 300 L0 300 Z" fill="url(#waveBlue)"/>
    </svg>

    <div class="brand">
      <span class="brand-square"></span>
      <span class="brand-name">Verdolith</span>
    </div>
    <p class="tagline">New Drugs from Herbal Medicines</p>

    <div class="identity">
      <p class="person-name">Soojin Park</p>
      <p class="person-title">President</p>
      <p class="address">5817 Briarwood DR<br>Fort Wayne, IN 46825 USA</p>
    </div>

    <div class="divider"></div>

    <ul class="contacts">
      <li>
        <svg class="contact-icon" viewBox="0 0 18 18"><circle cx="9" cy="9" r="9" fill="#2b3f6e"/><path d="M6 5 L8 5 L8.5 7.5 L7.3 8.2 Q8 10 9.8 10.7 L10.5 9.5 L13 10 L13 12 Q8 13 5 6 Z" fill="#fff"/></svg>
        260-555-0142
      </li>
      <li>
        <svg class="contact-icon" viewBox="0 0 18 18"><circle cx="9" cy="9" r="9" fill="#2b3f6e"/><rect x="6" y="4" width="6" height="10" rx="1" fill="#fff"/></svg>
        260-555-0187
      </li>
      <li>
        <svg class="contact-icon" viewBox="0 0 18 18"><circle cx="9" cy="9" r="9" fill="#2b3f6e"/><rect x="5" y="6" width="8" height="6" fill="#fff"/><rect x="6.5" y="4" width="5" height="2" fill="#fff"/></svg>
        260-555-0199
      </li>
      <li class="gap-before">
        <svg class="contact-icon" viewBox="0 0 18 18"><circle cx="9" cy="9" r="9" fill="#2b3f6e"/><rect x="4.5" y="5.5" width="9" height="7" fill="#fff"/><path d="M4.5 5.5 L9 9.5 L13.5 5.5" stroke="#2b3f6e" fill="none"/></svg>
        president@verdolith.com
      </li>
      <li>
        <svg class="contact-icon" viewBox="0 0 18 18"><circle cx="9" cy="9" r="9" fill="#2b3f6e"/><circle cx="9" cy="9" r="5" fill="none" stroke="#fff"/><path d="M4 9 H14 M9 4 V14" stroke="#fff"/></svg>
        www.verdolith.com
      </li>
    </ul>

    <p class="verse">And by the river upon the bank thereof, on this side and on that side, shall grow all trees for meat, whose leaf shall not fade, neither shall the fruit thereof be consumed: it shall bring forth new fruit according to his months, because their waters they issued out of the sanctuary: and the fruit thereof shall be for meat, and the leaf thereof for medicine. Ezekiel 47:12</p>
  </div>
</body>
</html>
```